bottle label/ product label for smoothies (ultra fresh)

Please create a bottle label for our smoothies for retail distribution.
It's important that the following key features are clearly stated:

Ultra-fresh

Handmade

No preservatives

Not heat-treated

No added sugar

The base of the product label should be transparent, so that the color and content of the smoothie can be seen clearly.

We are a young, dynamic company. Our values are honesty, ultra-freshness, and authenticity — and we are the only ones producing this type of product in our country. We are positioned in the premium segment.

Design style: Modern, clean, and natural — but not playful or childish.

Example product: Kelu Kelu (Mango, Pineapple, Lemon, Passion Fruit, Orange)

Wenn du möchtest, kann ich auch gleich einen konkreten Vorschlag für das Etikettendesign auf Englisch oder einen Entwurfstext für das Label selbst erstellen. Sag einfach Bescheid!

Target Market(s)

trade - convenience

Industry/Entity Type

trade

Font styles to use
Sans Serif

Requirements
Must have
• sales- features: Ultra-fresh Handmade No preservatives Not heat-treated No added sugar

```html
<!DOCTYPE html>
<html lang="en">
<head>
<meta charset="utf-8">
<title>Nuvelle Premium Smoothie – Mango Label</title>
<link href="https://fonts.googleapis.com/css2?family=Montserrat:wght@400;500&family=Poppins:wght@500&family=Yellowtail&display=swap" rel="stylesheet">
<style>
  :root {
    --canvas-bg: #dcdcdc;
    --band-dark: #262626;
    --band-light: #4a4a4a;
    --panel: #ececec;
    --brand-white: #f4f4f4;
    --gold: #d79a2c;
    --mango-orange: #e28a2a;
    --mango-yellow: #f2b431;
    --ink: #1e1e1e;
    --badge-grey: #5a5a5a;
  }
  * { margin: 0; padding: 0; box-sizing: border-box; }
  html, body {
    width: 1200px;
    height: 1200px;
    overflow: hidden;
    background: var(--canvas-bg);
  }
  .label {
    position: absolute;
    left: 300px;
    top: 42px;
    width: 600px;
    height: 1115px;
    border-radius: 44px;
    overflow: hidden;
    background: var(--panel);
    font-family: "Montserrat", sans-serif;
  }
  .label__band {
    position: absolute;
    left: 0; top: 0;
    width: 100%;
    height: 315px;
    background: linear-gradient(90deg, var(--band-dark) 0%, var(--band-dark) 45%, var(--band-light) 100%);
  }
  .brand-name {
    position: absolute;
    left: 0; right: 0;
    top: 80px;
    text-align: center;
    font-family: "Poppins", sans-serif;
    font-weight: 500;
    font-size: 96px;
    line-height: 1;
    letter-spacing: -1px;
    color: var(--brand-white);
  }
  .brand-tagline {
    position: absolute;
    left: 0; right: 0;
    top: 202px;
    text-align: center;
    font-weight: 400;
    font-size: 33px;
    letter-spacing: 4px;
    color: var(--gold);
  }
  .fruit-illustration {
    position: absolute;
    left: 160px;
    top: 405px;
    width: 280px;
    height: 340px;
    border-radius: 50% 50% 46% 46%;
    background: radial-gradient(circle at 40% 40%, var(--mango-yellow) 0%, var(--mango-orange) 85%);
  }
  .flavour-name {
    position: absolute;
    left: 0; right: 0;
    top: 740px;
    text-align: center;
    font-family: "Yellowtail", cursive;
    font-size: 112px;
    line-height: 1;
    color: var(--mango-orange);
  }
  .claims {
    position: absolute;
    left: 0; right: 0;
    top: 946px;
    text-align: center;
    list-style: none;
    font-weight: 500;
    font-size: 27px;
    line-height: 38px;
    color: var(--ink);
  }
  .badge {
    position: absolute;
    top: 928px;
    width: 116px;
    height: 116px;
  }
  .badge--fresh { left: 18px; }
  .badge--handmade { right: 18px; }
  .badge text {
    font-family: "Montserrat", sans-serif;
    font-weight: 500;
    font-size: 13px;
    letter-spacing: 1.5px;
    fill: var(--badge-grey);
  }
</style>
</head>
<body>
  <main class="label">
    <header class="label__band">
      <div class="brand-name">Nuvelle</div>
      <div class="brand-tagline">PREMIUM SMOOTHIE</div>
    </header>

    <div class="fruit-illustration" role="img" aria-label="Illustration of a ripe mango with a green leaf"></div>

    <div class="flavour-name">Mango</div>

    <svg class="badge badge--fresh" viewBox="0 0 116 116" aria-label="Ultra-fresh">
      <defs>
        <path id="fresh-arc" d="M14,58 A44,44 0 0,0 102,58"/>
      </defs>
      <path d="M18,54 A40,40 0 0,1 98,54" fill="none" stroke="var(--badge-grey)" stroke-width="3" stroke-linecap="round"/>
      <path d="M58,76 C44,70 42,54 50,44 C60,50 62,64 58,76 Z" fill="var(--badge-grey)"/>
      <path d="M58,76 C72,70 76,56 70,46 C62,52 56,64 58,76 Z" fill="var(--badge-grey)"/>
      <text><textPath href="#fresh-arc" startOffset="50%" text-anchor="middle">ULTRA-FRESH</textPath></text>
    </svg>

    <ul class="claims">
      <li>NO PRESERVATIVES</li>
      <li>NOT HEAT-TREATED</li>
      <li>NO ADDED SUGAR</li>
    </ul>

    <svg class="badge badge--handmade" viewBox="0 0 116 116" aria-label="Handmade">
      <defs>
        <path id="hand-arc" d="M14,58 A44,44 0 0,0 102,58"/>
      </defs>
      <path d="M18,54 A40,40 0 0,1 98,54" fill="none" stroke="var(--badge-grey)" stroke-width="3" stroke-linecap="round"/>
      <path d="M58,52 C52,46 46,50 50,55 L58,62 L66,55 C70,50 64,46 58,52 Z" fill="var(--badge-grey)"/>
      <path d="M40,70 L52,68 C56,67 60,70 62,72 L72,66 C76,64 79,68 76,71 L64,80 L44,80 Z" fill="var(--badge-grey)"/>
      <text><textPath href="#hand-arc" startOffset="50%" text-anchor="middle">HANDMADE</textPath></text>
    </svg>
  </main>
</body>
</html>
```